Carte d'affaire bilingue

Nous avons besoin d'une carte d'affaire pour notre entreprise spécialisée en vente et achat de terrain. Nous sommes une agence immobilière et nous voulons une carte avec le recto en Français et le verso en anglais. Nous voulons une image sobre et épurée. Nous avons de la clientèle internationale et nous voulons une carte très professionnelle mais qui se démarque. Nous voulons cibler une clientèle commerciale, industrielle, contracteurs et promoteurs immobiliers.

Hi everybody, we saw all your conception and we are approching of what we like but the "WOW" is missing.

We love the little sign to specify (phone or email) but we can put them in a square to make like our logo, we love also dark gray not lite gray, we also love the stainless lines. In our logo you can see a little sign +. For us is signyfy " Always further" so if you can put many little +++++ in the conception somewhere very discret it will be appreciate. We also like a kind of round that make a magnyfying glass, because we search land we found opportunity.

Thank you

Reason: I ask different things in the last day but no one do what i am asking for. For the conception # 3016702 that we love we ask changes.

We like simplicity, urban design, corporate, international. The card must have one side in french and the other side in english. We like dark gray,silver, and a little bit of green.

Target Market(s)

Investors, developers, construction builders, etc...

Font styles to use
Serif
Sans Serif

Requirements
Must have
• logo
La mention: Agence immobilière (Francais) / Real Estate Agency (anglais)
Sous le nom: Courtier immobilier agréé (Français) / Real Estate Broker

```html
<!DOCTYPE html>
<html lang="fr">
<head>
<meta charset="utf-8">
<title>Repère Foncier – Carte d'affaires</title>
<link rel="stylesheet" href="https://fonts.googleapis.com/css2?family=Questrial&family=Mulish:wght@700&display=swap">
<style>
  :root {
    --page: #ffffff;
    --card: #ffffff;
    --pattern-a: #fbfbfa;
    --pattern-b: #f1f2ef;
    --green: #1f7a3a;
    --green-dark: #17652f;
    --charcoal: #3d3f3e;
    --gray: #7a7c7b;
    --silver: #b9bcba;
    --edge: #e2e3e1;
  }
  * { box-sizing: border-box; margin: 0; padding: 0; }
  html, body { width: 1200px; height: 960px; overflow: hidden; background: var(--page); }
  body {
    font-family: "Questrial", "Century Gothic", sans-serif;
    display: flex; flex-direction: column; align-items: center; justify-content: center; gap: 56px;
  }
  .card {
    position: relative; width: 700px; height: 400px;
    background: var(--card);
    border: 1px solid var(--edge);
    box-shadow: 0 6px 18px rgba(0,0,0,0.08);
    overflow: hidden;
  }
  .card__pattern {
    position: absolute; inset: 0;
    background: radial-gradient(ellipse at 60% 70%, var(--pattern-b), var(--pattern-a) 75%);
  }
  .brand {
    position: absolute; left: 48px; top: 40px;
    display: flex; align-items: center; gap: 16px;
  }
  .brand__square { width: 58px; height: 58px; background: var(--green); }
  .brand__name {
    font-family: "Questrial", sans-serif; font-size: 40px; color: var(--charcoal);
    letter-spacing: 1px; line-height: 1;
  }
  .brand__mention {
    position: absolute; left: 122px; top: 112px;
    font-size: 19px; color: var(--charcoal);
    border-top: 1px solid var(--silver); padding-top: 4px;
  }
  .person { position: absolute; left: 48px; top: 168px; }
  .person__name { font-size: 30px; color: var(--green); margin-bottom: 6px; }
  .person__title { font-size: 19px; color: var(--gray); line-height: 1.3; }
  .address {
    position: absolute; left: 48px; bottom: 52px;
    font-size: 17px; color: var(--charcoal); line-height: 1.45;
  }
  .contact {
    position: absolute; right: 48px; bottom: 40px; text-align: right;
    font-size: 17px; color: var(--charcoal); line-height: 1.4; list-style: none;
  }
  .contact__label { font-family: "Mulish", sans-serif; font-weight: 700; color: var(--green-dark); }
</style>
</head>
<body>

  <article class="card card--fr" lang="fr">
    <div class="card__pattern" role="img" aria-label="Motif discret de petits signes plus gris sur fond blanc"></div>
    <div class="brand">
      <span class="brand__square"></span>
      <span class="brand__name">Repère Foncier</span>
    </div>
    <p class="brand__mention">Agence immobilière</p>
    <div class="person">
      <h1 class="person__name">Maryse Delorme</h1>
      <p class="person__title">Courtier Immobilier Agréé, D.A.<br>Vice Présidente</p>
    </div>
    <address class="address">27 B, boul. des Érables, 2e<br>Laval, Qc, H7T 0A1</address>
    <ul class="contact">
      <li>www.reperefoncier.com</li>
      <li>m.delorme@reperefoncier.com</li>
      <li><span class="contact__label">Téléphone</span> 514.555.0148</li>
      <li><span class="contact__label">Télécopie</span> 450.555.0193</li>
      <li><span class="contact__label">Sans Frais</span> 1.800.555.0162</li>
    </ul>
  </article>

  <article class="card card--en" lang="en">
    <div class="card__pattern" role="img" aria-label="Subtle pattern of small grey plus signs on white"></div>
    <div class="brand">
      <span class="brand__square"></span>
      <span class="brand__name">Parcel Compass</span>
    </div>
    <p class="brand__mention">Real Estate Agency</p>
    <div class="person">
      <h1 class="person__name">Maryse Delorme</h1>
      <p class="person__title">Real Estate Broker, D.A.<br>Vice President</p>
    </div>
    <address class="address">27 B, boul. des Érables, 2e<br>Laval, Qc, H7T 0A1</address>
    <ul class="contact">
      <li>www.reperefoncier.com</li>
      <li>m.delorme@reperefoncier.com</li>
      <li><span class="contact__label">Phone</span> 514.555.0148</li>
      <li><span class="contact__label">Fax</span> 450.555.0193</li>
      <li><span class="contact__label">Toll Free</span> 1.800.555.0162</li>
    </ul>
  </article>

</body>
</html>
```